Four in One (Flexible infographic for Content Management Industry)

See attachment.
A graphic depicting 4 products, where each can stand on its own and each can be combined with others, but where, if all are taken together, the best result is achieved (the "super product").
Intended use is web. See attached file as an example.
The most basic idea is as the attached diagram shows, where 4 rectangles are arranged in a quadrangle, with a middle rectangle in the center representing the combined 4 products. This concept is fine except it is a bit too obvious as it stands. We are looking for either a variation of this or another concept.
The audience is technical + professional + enterprise - NOT consumers. Hence the design should be conservative in nature.
We are aware of tools like as Canva or Pictogram where such graphics are available, but we are looking for something with a bit more imagination and flexibility.
This graphic should be targeted to web sites and be delivered with vector-based (SVG) graphics.

```html
<!DOCTYPE html>
<html lang="en">
<head>
<meta charset="utf-8">
<title>Four in One – Super Product</title>
<link href="https://fonts.googleapis.com/css2?family=Poppins:wght@400;500;600;700;800&display=swap" rel="stylesheet">
<style>
:root{
  --red:#e7383a;
  --yellow:#f5c314;
  --blue:#2189cb;
  --teal:#14b3a8;
  --frame-dark:#dcdcde;
  --frame-light:#f7f7f8;
  --ink:#2f2f31;
  --white:#ffffff;
}
*{box-sizing:border-box;margin:0;padding:0}
html,body{width:1200px;height:908px;overflow:hidden;background:var(--white)}
body{font-family:"Poppins",sans-serif;color:var(--white);position:relative}

.frame{position:absolute;width:500px;height:288px;background:linear-gradient(180deg,var(--frame-dark),var(--frame-light) 40%,var(--frame-light) 60%,var(--frame-dark))}
.frame--tl{left:107px;top:151px;border-radius:0 62px 0 62px}
.frame--tr{left:637px;top:151px;width:457px;border-radius:62px 0 62px 0}
.frame--bl{left:107px;top:470px;border-radius:62px 0 62px 0}
.frame--br{left:637px;top:470px;width:457px;border-radius:0 62px 0 62px}

.card{position:absolute;height:235px;padding:0 26px}
.card--docs{left:132px;top:178px;width:449px;background:var(--red);border-radius:0 26px 0 26px}
.card--security{left:663px;top:178px;width:406px;background:var(--yellow);border-radius:26px 0 26px 0;text-align:right;padding-left:16px}
.card--erp{left:132px;top:495px;width:449px;background:var(--blue);border-radius:26px 0 26px 0}
.card--digital{left:663px;top:495px;width:406px;background:var(--teal);border-radius:0 26px 0 26px;text-align:right}

.card__title{font-weight:700;font-size:18px;line-height:1;letter-spacing:-.1px;margin-top:31px;white-space:nowrap}
.card__text{font-size:10.6px;line-height:12.6px;margin-top:7px;white-space:nowrap}
.card--security .card__text{letter-spacing:-.15px;margin-top:5px}
.card__rule{display:block;width:72px;height:2px;background:var(--white);margin-top:6px}
.card--security .card__rule,.card--digital .card__rule{margin-left:auto}
.card__list{list-style:none;margin-top:8px;font-size:10.6px;white-space:nowrap}
.card__list li{line-height:19.2px}
.card__link{display:inline-block;margin-top:11px;font-size:10.6px;font-weight:500;color:var(--white);text-decoration:none}
.card--erp .card__title{margin-top:28px}
.card--digital .card__title{margin-top:38px}
.card--digital .card__list{margin-top:7px}
.card--digital .card__link{margin-top:7px}

.hub{position:absolute;left:0;top:0}
.hub__label{position:absolute;left:512px;top:420px;width:200px;text-align:center;color:var(--ink);line-height:1}
.hub__label b{display:block;font-weight:800;font-size:29px}
.hub__label span{display:block;font-weight:600;font-size:28px;margin-top:6px;letter-spacing:.5px}
</style>
</head>
<body>

<div class="frame frame--tl"></div>
<div class="frame frame--tr"></div>
<div class="frame frame--bl"></div>
<div class="frame frame--br"></div>

<section class="card card--docs">
  <h2 class="card__title">Document Management</h2>
  <p class="card__text">Streamline document organization access, and collaboration with easier<br>file storage and sharing, leading to more efficient workflows</p>
  <span class="card__rule"></span>
  <ul class="card__list">
    <li>✓ Centralized Document Control</li>
    <li>✓ Collaborative Workspace Integration</li>
    <li>✓ Automated Compliance Tracking</li>
    <li>✓ Check</li>
  </ul>
  <a class="card__link" href="#">Learn More ▸</a>
</section>

<section class="card card--security">
  <h2 class="card__title">Security and Compliance</h2>
  <p class="card__text">Benefit from tailored cloud solutions, secure data storage, and expert<br>disaster recovery planning for reliable and scalable IT operations.</p>
  <span class="card__rule"></span>
  <ul class="card__list">
    <li>Custom Cloud Solutions ✓</li>
    <li>Secure Data Storage ✓</li>
    <li>Expert Disaster Recovery ✓</li>
    <li>Check ✓</li>
  </ul>
  <a class="card__link" href="#">Learn More ▸</a>
</section>

<section class="card card--erp">
  <h2 class="card__title">Enterprise Resource Planning</h2>
  <p class="card__text">Simplify management across finance, sales,<br>and operations, enabling better decision-making<br>and improved productivity.</p>
  <span class="card__rule"></span>
  <ul class="card__list">
    <li>✓ Integrated Business Processes</li>
    <li>✓ Enhanced Decision-Making</li>
    <li>✓ Productivity improvement</li>
    <li>✓ Check</li>
  </ul>
  <a class="card__link" href="#">Learn More ▸</a>
</section>

<section class="card card--digital">
  <h2 class="card__title">Digitital Transformation</h2>
  <p class="card__text">Turn scanned documents into easily<br>searchabledigital archives, boosting efficiency<br>and accessibility.</p>
  <span class="card__rule"></span>
  <ul class="card__list">
    <li>Instant searchable Archives with OCR ✓</li>
    <li>Automated Document Classification ✓</li>
    <li>Vaultline and Cloud Blob Ready ✓</li>
    <li>Check ✓</li>
  </ul>
  <a class="card__link" href="#">Learn More ▸</a>
</section>

<svg class="hub" width="1200" height="908" viewBox="0 0 1200 908" aria-hidden="true">
  <defs>
    <radialGradient id="disk" cx="0.65" cy="0.3" r="0.85">
      <stop offset="0" stop-color="#ffffff"/>
      <stop offset="0.5" stop-color="#ededee"/>
      <stop offset="1" stop-color="#b9b8bb"/>
    </radialGradient>
    <filter id="soft" x="-30%" y="-30%" width="160%" height="160%">
      <feDropShadow dx="0" dy="4" stdDeviation="6" flood-color="#000" flood-opacity=".25"/>
    </filter>
  </defs>

  <circle class="hub__ring" cx="612" cy="454" r="121" fill="rgba(255,255,255,0.12)" stroke="#9a9a9c" stroke-width="1.2"/>
  <circle cx="612" cy="454" r="104" fill="rgba(0,0,0,0.06)"/>
  <circle class="hub__disk" cx="612" cy="454" r="99" fill="url(#disk)" stroke="#fff" stroke-width="3" filter="url(#soft)"/>

  <g class="hub__nodes" fill="#fff">
    <circle cx="522" cy="374" r="5.5"/>
    <circle cx="703" cy="374" r="5.5"/>
    <circle cx="522" cy="533" r="5.5"/>
    <circle cx="703" cy="533" r="5.5"/>
  </g>

  <g class="badge badge--docs" transform="translate(478 350)">
    <path d="M18 22 L33 19 L22 12 Z" fill="#fff"/>
    <circle r="29" fill="#fff" filter="url(#soft)"/>
    <circle r="23" fill="var(--red)"/>
    <g fill="none" stroke="#fff" stroke-width="1.4" stroke-linejoin="round">
      <path d="M-12 -8 v20 h24 v-16 h-12 l-3 -4 z"/>
      <path d="M-8 -4 v-9 h15 v9"/>
      <path d="M-5 -9 h8 M-5 -6 h8"/>
      <path d="M3 8 h6"/>
    </g>
  </g>

  <g class="badge badge--security" transform="translate(746 350)">
    <path d="M-18 22 L-33 19 L-22 12 Z" fill="#fff"/>
    <circle r="29" fill="#fff" filter="url(#soft)"/>
    <circle r="23" fill="var(--yellow)"/>
    <g fill="none" stroke="#fff" stroke-width="1.4" stroke-linejoin="round">
      <rect x="-11" y="-13" width="17" height="24" rx="1.5"/>
      <rect x="-8" y="-8" width="6" height="5"/>
      <path d="M-7 -8 v-2 a2 2 0 0 1 4 0 v2"/>
      <path d="M0 -7 h3 M0 -4 h3 M-8 2 h11 M-8 6 h8"/>
    </g>
    <path d="M6 -1 l7 2.5 v5 c0 4 -3 6 -7 7.5 c-4 -1.5 -7 -3.5 -7 -7.5 v-5 z" fill="#fff"/>
    <path d="M3 6 l2.5 2.5 l4 -4.5" fill="none" stroke="var(--yellow)" stroke-width="1.5"/>
  </g>

  <g class="badge badge--erp" transform="translate(478 557)">
    <path d="M18 -22 L33 -19 L22 -12 Z" fill="#fff"/>
    <circle r="29" fill="#fff" filter="url(#soft)"/>
    <circle r="23" fill="var(--blue)"/>
    <g fill="none" stroke="#fff" stroke-width="1.4" stroke-linejoin="round">
      <path d="M-2 -14 h4 l1 4 l3 1.5 l3.5 -2 l3 3 l-2 3.5 l1.5 3 l4 1 v4 l-4 1 l-1.5 3 l2 3.5 l-3 3 l-3.5 -2 l-3 1.5 l-1 4 h-4 l-1 -4 l-3 -1.5 l-3.5 2 l-3 -3 l2 -3.5 l-1.5 -3 l-4 -1 v-4 l4 -1 l1.5 -3 l-2 -3.5 l3 -3 l3.5 2 l3 -1.5 z"/>
      <circle r="8"/>
      <path d="M-4 5 l6 -6 a3.5 3.5 0 1 1 3 3 l-6 6 z"/>
    </g>
  </g>

  <g class="badge badge--digital" transform="translate(746 557)">
    <path d="M-18 -22 L-33 -19 L-22 -12 Z" fill="#fff"/>
    <circle r="29" fill="#fff" filter="url(#soft)"/>
    <circle r="23" fill="var(--teal)"/>
    <g fill="none" stroke="#fff" stroke-width="1.4" stroke-linejoin="round">
      <path d="M-2 -14 h4 l1 4 l3 1.5 l3.5 -2 l3 3 l-2 3.5 l1.5 3 l4 1 v4 l-4 1 l-1.5 3 l2 3.5 l-3 3 l-3.5 -2 l-3 1.5 l-1 4 h-4 l-1 -4 l-3 -1.5 l-3.5 2 l-3 -3 l2 -3.5 l-1.5 -3 l-4 -1 v-4 l4 -1 l1.5 -3 l-2 -3.5 l3 -3 l3.5 2 l3 -1.5 z"/>
      <circle r="7"/>
      <path d="M-7 0 h-6 M0 -7 v-3 M5 5 l3 3 M-5 -5 l-3 -3"/>
    </g>
    <g fill="#fff"><circle r="2"/><circle cx="-13" r="1.6"/></g>
  </g>
</svg>

<div class="hub__label"><b>SUPER</b><span>PRODUCT</span></div>

</body>
</html>
```